Brevin Electric Ltd

Looking for a single page website and Facebook page design. I am an electrical contractor based on Vancouver Island. I do service, custom homes, residential and commercial installations. My company just started out, so I don't have any pictures of installs yet. I have 25 years experience. I would like the colors to be my logo colors black and I have a black Torvik Ridgeman that will be my vehicle which I will have a wrap for.
Updates

I just posted the contest today, not sure why the deadline is the same day.

Went on vacation/holiday

Industry/Entity Type

Electrician

Requirements
Must have
• Services provided, About me section, quote section,
Nice to have
• I am not quite sure yet, I need to see some designs first .

```html
<!DOCTYPE html>
<html lang="en">
<head>
<meta charset="utf-8">
<title>Brevin Electric Ltd</title>
<link rel="stylesheet" href="https://fonts.googleapis.com/css2?family=Montserrat:wght@600;700&family=Roboto:wght@400;700&display=swap">
<style>
  :root {
    --gold: #f5b91a;
    --white: #ffffff;
    --ink: #161616;
    --band: rgba(38, 38, 38, 0.86);
    --photo-dark: #141210;
    --photo-mid: #3a332c;
    --photo-warm: #5a4a30;
  }
  * { box-sizing: border-box; margin: 0; padding: 0; }
  html, body { width: 1200px; height: 527px; overflow: hidden; background: var(--ink); }
  .banner {
    position: relative; width: 1200px; height: 527px; overflow: hidden;
    font-family: "Roboto", Arial, sans-serif; color: var(--white);
  }
  .banner__backdrop {
    position: absolute; inset: 0;
    background:
      radial-gradient(ellipse at 30% 60%, var(--photo-warm) 0%, transparent 55%),
      radial-gradient(ellipse at 80% 30%, var(--photo-mid) 0%, transparent 60%),
      linear-gradient(160deg, var(--photo-mid) 0%, var(--photo-dark) 70%);
    opacity: 0.9;
  }
  .brand {
    position: absolute; left: 41px; top: 31px;
    display: flex; align-items: center; gap: 22px;
  }
  .brand__dot {
    width: 72px; height: 72px; border-radius: 50%;
    border: 4px solid var(--gold);
  }
  .brand__name {
    font-family: "Montserrat", Arial, sans-serif; font-weight: 600;
    font-size: 25px; color: var(--white); letter-spacing: 0.3px;
  }
  .service-band {
    position: absolute; left: 0; top: 154px; width: 1200px; height: 219px;
    background: var(--band);
  }
  .service {
    position: absolute; top: 58px; width: 200px; margin-left: -100px;
    display: flex; flex-direction: column; align-items: center;
  }
  .service__icon { width: 70px; height: 70px; }
  .service__label {
    margin-top: 27px; font-weight: 700; font-size: 21px; letter-spacing: 0.2px;
  }
  .emblem {
    position: absolute; left: 746px; top: 114px; width: 396px; height: 266px;
  }
  .contact {
    position: absolute; display: flex; align-items: center; gap: 28px;
  }
  .contact__icon {
    flex: none; width: 50px; height: 50px; border-radius: 50%;
    background: var(--gold); display: flex; align-items: center; justify-content: center;
  }
  .contact__icon svg { width: 24px; height: 24px; }
  .contact__text { font-size: 19px; line-height: 30px; }
  .contact--address { left: 15px; top: 446px; gap: 29px; }
  .contact--phone { left: 426px; top: 455px; gap: 29px; }
  .contact--email { left: 768px; top: 449px; gap: 32px; }
  .contact--email .contact__text { font-size: 20px; }
</style>
</head>
<body>
<main class="banner">
  <div class="banner__backdrop" role="img" aria-label="Dimmed photograph of an open electrical panel with coloured wiring and an electrician's hands"></div>

  <header class="brand">
    <span class="brand__dot"></span>
    <span class="brand__name">BREVIN ELECTRIC Ltd</span>
  </header>

  <section class="service-band">
    <div class="service" style="left:88px">
      <svg class="service__icon" viewBox="0 0 64 64" fill="none" stroke="var(--gold)" stroke-width="2.4" stroke-linejoin="round">
        <path d="M28 6h8l1.5 6 5 2 5.3-3.3 5.6 5.6L50 21.6l2 5 6 1.4v8l-6 1.5-2 5 3.3 5.3-5.6 5.6L42.4 50l-5 2L36 58h-8l-1.5-6-5-2-5.3 3.3-5.6-5.6L14 42.4l-2-5L6 36v-8l6-1.5 2-5-3.3-5.3 5.6-5.6L21.6 14l5-2z"/>
        <circle cx="32" cy="32" r="11"/>
        <circle cx="32" cy="32" r="4"/>
      </svg>
      <span class="service__label">SERVICES</span>
    </div>
    <div class="service" style="left:274px">
      <svg class="service__icon" viewBox="0 0 64 64" fill="none" stroke="var(--gold)" stroke-width="2.4" stroke-linejoin="round">
        <path d="M6 28 32 8l26 20"/>
        <path d="M12 24v34h40V24"/>
        <rect x="18" y="32" width="10" height="9"/>
        <rect x="36" y="32" width="10" height="9"/>
        <path d="M27 58V47h10v11"/>
        <path d="M6 58h52"/>
      </svg>
      <span class="service__label">RESIDENTIAL</span>
    </div>
    <div class="service" style="left:484px">
      <svg class="service__icon" viewBox="0 0 64 64" fill="none" stroke="var(--gold)" stroke-width="2.4" stroke-linejoin="round">
        <rect x="8" y="26" width="16" height="32"/>
        <rect x="24" y="8" width="18" height="50"/>
        <rect x="42" y="20" width="14" height="38"/>
        <path d="M13 33h6M13 40h6M13 47h6M29 15h8M29 22h8M29 29h8M29 36h8M29 43h8M46 27h6M46 34h6M46 41h6M4 58h56"/>
      </svg>
      <span class="service__label">COMMERCIAL</span>
    </div>
    <div class="service" style="left:675px">
      <svg class="service__icon" viewBox="0 0 64 64" fill="none" stroke="var(--gold)" stroke-width="2.4" stroke-linejoin="round">
        <path d="M8 14h44v42H8z"/>
        <path d="M8 14c0-4 4-6 6-6s6 2 6 6"/>
        <path d="M16 24h16v14H16zM32 30h12M24 38v10"/>
        <path d="M40 46l16-16 4 4-16 16-6 2z"/>
      </svg>
      <span class="service__label">PROJECT</span>
    </div>

  </section>

  <svg class="emblem" viewBox="0 0 396 266" role="img" aria-label="Brevin Electric Ltd">
    <ellipse cx="198" cy="133" rx="190" ry="125" fill="none" stroke="var(--gold)" stroke-width="8"/>
    <text x="198" y="142" text-anchor="middle" font-family="Montserrat, Arial, sans-serif" font-weight="600" font-size="28" fill="var(--white)">BREVIN ELECTRIC Ltd</text>
  </svg>

  <div class="contact contact--address">
    <span class="contact__icon">
      <svg viewBox="0 0 24 24" fill="var(--white)"><path d="M12 2a7 7 0 0 0-7 7c0 5 7 13 7 13s7-8 7-13a7 7 0 0 0-7-7zm0 9.5A2.5 2.5 0 1 1 12 6.5a2.5 2.5 0 0 1 0 5z"/></svg>
    </span>
    <p class="contact__text">123,Lorem ipsum dolor sit amet,<br>tetur adipiscing elit</p>
  </div>

  <div class="contact contact--phone">
    <span class="contact__icon">
      <svg viewBox="0 0 24 24" fill="var(--white)"><path d="M6.6 10.8a15.1 15.1 0 0 0 6.6 6.6l2.2-2.2a1 1 0 0 1 1-.25 11.4 11.4 0 0 0 3.6.57 1 1 0 0 1 1 1V20a1 1 0 0 1-1 1A17 17 0 0 1 3 4a1 1 0 0 1 1-1h3.5a1 1 0 0 1 1 1c0 1.25.2 2.45.57 3.57a1 1 0 0 1-.25 1z"/></svg>
    </span>
    <p class="contact__text">Phone : +1 888 888 8888</p>
  </div>

  <div class="contact contact--email">
    <span class="contact__icon">
      <svg viewBox="0 0 24 24" fill="var(--white)"><path d="M3 5h18a1 1 0 0 1 1 1v1l-10 6L2 7V6a1 1 0 0 1 1-1zm-1 4.3 10 6 10-6V18a1 1 0 0 1-1 1H3a1 1 0 0 1-1-1z"/></svg>
    </span>
    <p class="contact__text">Email : info@companyname.com</p>
  </div>
</main>
</body>
</html>
```